Business Card Design

Hunting Ranch in the Texas hill country (Deer, Turkey, Quail)

Want Walter on one side and Gloria on the other.
We are looking for a Jack Rabbit NOT a cottontail bunny

Industry/Entity Type

Business

Contact Information for Business Card

Copper Mesa Ranch
Junction Texas
Walter Krimsley Gloria Krimsley
14 Paloverde Hollow Ct. 14 Paloverde Hollow Ct.
The Woodlands, Texas U.S.A. The Woodlands, Texas U.S.A.
281-555-0143 281-555-0187

```html
<!DOCTYPE html>
<html lang="en">
<head>
<meta charset="utf-8">
<title>Copper Mesa Ranch – Business Card</title>
<link rel="stylesheet" href="https://fonts.googleapis.com/css2?family=Cabin+Sketch:wght@400;700&family=Delius&display=swap">
<style>
  :root {
    --cream: #f9e3c8;
    --sand: #e9ccaa;
    --tan: #b89068;
    --earth: #7b5535;
    --dark-earth: #5e3f24;
    --ink: #5a2c12;
    --white: #ffffff;
    --grass-dark: #4a5220;
    --grass-mid: #6e6a2c;
    --hare-gold: #c9903a;
    --hare-brown: #5a2c14;
  }
  html, body {
    margin: 0;
    padding: 0;
    width: 1200px;
    height: 702px;
    overflow: hidden;
    background: var(--white);
  }
  .card {
    position: relative;
    width: 1200px;
    height: 702px;
    overflow: hidden;
    background: linear-gradient(to bottom,
      var(--cream) 0%,
      var(--cream) 40%,
      var(--sand) 50%,
      var(--tan) 68%,
      var(--earth) 85%,
      var(--dark-earth) 100%);
  }
  .brand-name {
    position: absolute;
    left: 70px;
    top: 34px;
    margin: 0;
    font-family: "Cabin Sketch", cursive;
    font-weight: 700;
    font-size: 120px;
    line-height: 1;
    letter-spacing: 2px;
    color: var(--ink);
    white-space: nowrap;
  }
  .tagline {
    position: absolute;
    right: 77px;
    top: 174px;
    margin: 0;
    font-family: "Delius", cursive;
    font-size: 33px;
    line-height: 1;
    color: var(--ink);
    white-space: nowrap;
  }
  .address {
    position: absolute;
    left: 80px;
    top: 312px;
    margin: 0;
    font-family: "Delius", cursive;
    font-style: normal;
    font-size: 35px;
    line-height: 40px;
    color: var(--ink);
    white-space: nowrap;
  }
  .contact-name {
    position: absolute;
    left: 78px;
    top: 490px;
    margin: 0;
    font-family: "Cabin Sketch", cursive;
    font-weight: 700;
    font-size: 72px;
    line-height: 1;
    color: var(--white);
    white-space: nowrap;
  }
  .contact-phone {
    position: absolute;
    left: 78px;
    top: 586px;
    margin: 0;
    font-family: "Cabin Sketch", cursive;
    font-weight: 700;
    font-size: 46px;
    line-height: 1;
    color: var(--white);
    white-space: nowrap;
  }
  .grass-art {
    position: absolute;
    left: 0;
    top: 510px;
    width: 1200px;
    height: 192px;
    background: linear-gradient(to bottom,
      rgba(110, 106, 44, 0) 0%,
      rgba(110, 106, 44, 0.6) 40%,
      var(--grass-dark) 100%);
    -webkit-mask-image: linear-gradient(to right, transparent 0%, transparent 12%, #000 40%, #000 100%);
    mask-image: linear-gradient(to right, transparent 0%, transparent 12%, #000 40%, #000 100%);
  }
  .hares-art {
    position: absolute;
    left: 763px;
    top: 212px;
    width: 354px;
    height: 392px;
    border-radius: 40% 40% 14% 14%;
    background: radial-gradient(ellipse at 50% 60%,
      var(--hare-gold) 0%,
      #a8702e 45%,
      var(--hare-brown) 100%);
    opacity: 0.85;
  }
</style>
</head>
<body>
  <main class="card">
    <h1 class="brand-name">Copper Mesa Ranch</h1>
    <p class="tagline">Junction Texas Hunting Ranch</p>

    <div class="grass-art" role="img" aria-label="Illustrated tall prairie grass along the bottom of the card"></div>
    <div class="hares-art" role="img" aria-label="Illustration of two jackrabbits sitting side by side in the grass"></div>

    <address class="address">
      Copper Mesa Ranch<br>
      Junction Texas<br>
      14 Paloverde Hollow Ct<br>
      The Woodlands, Texas U.S.A.
    </address>

    <p class="contact-name">Walter Krimsley</p>
    <p class="contact-phone">(281) 555-0143</p>
  </main>
</body>
</html>
```